Business card for auto dealership

Looking for a clean modern design.
Would like attached logo incorporated

Industry/Entity Type

Car dealership

Contact Information for Business Card

Name, website, phone, cell, fax, email

```html
<!DOCTYPE html>
<html lang="en">
<head>
<meta charset="utf-8">
<title>Halvorsen Truck &amp; Auto Sales — Business Card</title>
<link href="https://fonts.googleapis.com/css2?family=Montserrat:wght@400;600;800&display=swap" rel="stylesheet">
<style>
  :root {
    --backdrop: #2a2a2c;
    --card: #1c1c1d;
    --card-edge: #3a3a3c;
    --silver: #e4e4e6;
    --silver-dim: #b9b9bd;
    --ghost: #252526;
    --text-sub: #9d9da2;
  }
  html, body {
    margin: 0;
    padding: 0;
    width: 1200px;
    height: 900px;
    overflow: hidden;
    background: var(--backdrop);
    font-family: "Montserrat", Arial, sans-serif;
  }
  .canvas {
    position: relative;
    width: 1200px;
    height: 900px;
  }
  .card {
    position: absolute;
    left: 320px;
    width: 560px;
    height: 320px;
    background: var(--card);
    border-radius: 18px;
    box-shadow: 0 0 0 1px var(--card-edge), 0 18px 40px rgba(0,0,0,.45);
    overflow: hidden;
  }
  .card--info { top: 100px; }
  .card--brand { top: 480px; }

  .ghost-name {
    position: absolute;
    right: 26px;
    top: 22px;
    font-weight: 800;
    font-size: 50px;
    line-height: 1;
    color: var(--ghost);
    transform: rotate(180deg);
    white-space: nowrap;
  }

  .brand {
    color: var(--silver);
    font-weight: 800;
    line-height: 1.05;
    letter-spacing: .5px;
  }
  .card--info .brand {
    position: absolute;
    left: 36px;
    top: 40px;
    font-size: 30px;
  }
  .brand__sub { display: block; font-size: .5em; letter-spacing: 2px; }

  .person {
    position: absolute;
    left: 36px;
    top: 140px;
    color: var(--silver);
  }
  .person__name { font-weight: 600; font-size: 20px; margin: 0; }
  .person__role { font-weight: 400; font-size: 13px; color: var(--text-sub); margin: 2px 0 12px; }

  .contact { list-style: none; margin: 0; padding: 0; }
  .contact li {
    display: flex;
    align-items: center;
    gap: 10px;
    font-size: 13px;
    color: var(--silver-dim);
    height: 21px;
  }
  .contact svg { width: 13px; height: 13px; fill: var(--silver); flex: none; }

  .card--brand {
    display: flex;
    align-items: center;
    justify-content: center;
  }
  .card--brand .brand {
    font-size: 50px;
    text-align: center;
  }
</style>
</head>
<body>
<main class="canvas">
  <section class="card card--info" aria-label="Card front with contact details">
    <div class="ghost-name" aria-hidden="true">Halvorsen</div>
    <div class="brand">Halvorsen<span class="brand__sub">TRUCK &amp; AUTO SALES</span></div>
    <div class="person">
      <p class="person__name">Casey Halvorsen</p>
      <p class="person__role">Owner</p>
      <ul class="contact">
        <li><svg viewBox="0 0 16 16"><path d="M3 1h3l1.5 4-2 1.2a9 9 0 0 0 4.3 4.3L11 8.5 15 10v3a2 2 0 0 1-2 2A12 12 0 0 1 1 3a2 2 0 0 1 2-2z"/></svg>555-210-3968</li>
        <li><svg viewBox="0 0 16 16"><path d="M4.5 0h7A1.5 1.5 0 0 1 13 1.5v13a1.5 1.5 0 0 1-1.5 1.5h-7A1.5 1.5 0 0 1 3 14.5v-13A1.5 1.5 0 0 1 4.5 0zM5 2v10h6V2zm3 11a1 1 0 1 0 0 2 1 1 0 0 0 0-2z"/></svg>555-384-7052</li>
        <li><svg viewBox="0 0 16 16"><path d="M4 1h6l2 2v3H4zM1 7h14v7H1zm2 2v1h2V9zm4 0v1h2V9zm4 0v1h2V9zM3 11v1h2v-1zm4 0v1h2v-1z"/></svg>555-617-2485</li>
        <li><svg viewBox="0 0 16 16"><path d="M1 3h14v10H1zm1.5 1.2L8 8.5l5.5-4.3z"/></svg>casey@halvorsenauto.com</li>
        <li><svg viewBox="0 0 16 16"><path d="M8 1a7 7 0 1 0 0 14A7 7 0 0 0 8 1zm0 1.5c.8 0 1.8 1.8 2 4.5H6c.2-2.7 1.2-4.5 2-4.5zM6 9h4c-.2 2.7-1.2 4.5-2 4.5S6.2 11.7 6 9z"/></svg>www.halvorsenauto.com</li>
      </ul>
    </div>
  </section>

  <section class="card card--brand" aria-label="Card back with company name">
    <div class="brand">Halvorsen<span class="brand__sub">TRUCK &amp; AUTO SALES</span></div>
  </section>
</main>
</body>
</html>
```